Cylinder Packaging Design - Massage Balls Sports company

Package design needed for 1 x massage and 1 x double massage balls. please see images attached of the 2 products, both items will be stored in 1 x cardboard cylinder tube, samples also attached please ignore the designs as its the style of packaging that you are referring to.

Size of cylinder, length 21cm width 7.5cm

Final design should communicate health and fitness / physiotherapy / rehabilitation but also relating to our retail sports company, logo colour ect. please refer to our website www.kq3active.com for your reference and also to give you an idea who we are and what we do.

Attached are our 2 logos 1 x black and 1 x grey back grounds for you to work with.

```html
<!DOCTYPE html>
<html lang="en">
<head>
<meta charset="utf-8">
<title>KQ3 Active – Lacrosse Massage Balls Tube Label</title>
<link rel="stylesheet" href="https://fonts.googleapis.com/css2?family=Roboto:wght@400;500&family=Roboto+Condensed:wght@300;700&display=swap">
<style>
  :root {
    --page-bg: #ececec;
    --label-bg: #f4f5f6;
    --label-edge: #e2e4e6;
    --brand-blue: #2f86c3;
    --brand-blue-dark: #1f6fae;
    --title-grey: #8aa0b2;
    --body-blue: #3f8fca;
    --list-grey: #4d5a66;
    --ball-yellow: #f1d62c;
    --ball-yellow-deep: #c9a80f;
    --band-light: #dfeaf3;
    --band-text: #ffffff;
  }
  * { margin: 0; padding: 0; box-sizing: border-box; }
  html, body { width: 800px; height: 1200px; overflow: hidden; }
  body {
    background: var(--page-bg);
    font-family: "Roboto", Arial, sans-serif;
    position: relative;
  }
  .tube-label {
    position: absolute;
    left: 190px; top: 150px;
    width: 420px; height: 900px;
    background: var(--label-bg);
    border: 1px solid var(--label-edge);
    overflow: hidden;
  }
  .brand {
    position: absolute;
    top: 150px; left: 0; right: 0;
    text-align: center;
    color: var(--brand-blue);
    font-family: "Roboto Condensed", Arial, sans-serif;
    font-weight: 700;
  }
  .brand-name { font-size: 64px; line-height: 1; letter-spacing: 1px; }
  .brand-sub { font-size: 15px; letter-spacing: 2px; margin-top: 4px; }
  .product-photo {
    position: absolute;
    right: 0; top: 300px;
    width: 190px; height: 470px;
    border-radius: 95px 0 0 95px;
    background: radial-gradient(ellipse at 40% 35%, #fbe96a 0%, var(--ball-yellow) 45%, var(--ball-yellow-deep) 100%);
  }
  .intro {
    position: absolute;
    left: 22px; top: 330px;
    width: 190px;
    color: var(--body-blue);
    font-size: 12px;
    line-height: 1.45;
  }
  .product-title {
    position: absolute;
    left: 22px; top: 520px;
    font-family: "Roboto Condensed", Arial, sans-serif;
  }
  .product-title .line-main {
    display: block;
    font-weight: 300;
    font-size: 58px;
    line-height: 1;
    color: var(--title-grey);
    letter-spacing: -1px;
  }
  .product-title .line-sub {
    display: block;
    font-weight: 700;
    font-size: 26px;
    color: var(--brand-blue);
    margin-top: 6px;
  }
  .benefits {
    position: absolute;
    left: 22px; top: 650px;
    list-style: none;
    color: var(--list-grey);
    font-size: 13px;
  }
  .benefits li {
    display: flex; align-items: center; gap: 7px;
    margin-bottom: 6px;
  }
  .benefits svg { width: 8px; height: 8px; flex: none; }
  .tagline-band {
    position: absolute;
    left: 0; right: 0; bottom: 70px;
    height: 40px;
    background: linear-gradient(90deg, var(--brand-blue-dark) 0%, var(--brand-blue) 55%, var(--band-light) 100%);
    color: var(--band-text);
    font-size: 17px;
    letter-spacing: 0.5px;
    display: flex; align-items: center;
    padding-left: 22px;
  }
</style>
</head>
<body>
  <section class="tube-label">
    <div class="brand">
      <div class="brand-name">KQ3</div>
      <div class="brand-sub">ACTIVE STORE</div>
    </div>

    <div class="product-photo" role="img" aria-label="Photo of a yellow double lacrosse massage ball with a dark band around its middle"></div>

    <p class="intro">Relieve tension, stimulate blood circulation, and ease pain with this set designed specifically for my official release.</p>

    <h1 class="product-title">
      <span class="line-main">LACROSSE</span>
      <span class="line-sub">MASSAGE BALLS</span>
    </h1>

    <ul class="benefits">
      <li><svg viewBox="0 0 8 8"><path d="M4 0v8M0 4h8" stroke="#8aa0b2" stroke-width="1.6"/></svg>Self Massage</li>
      <li><svg viewBox="0 0 8 8"><path d="M4 0v8M0 4h8" stroke="#8aa0b2" stroke-width="1.6"/></svg>Muscle Enhancement</li>
      <li><svg viewBox="0 0 8 8"><path d="M4 0v8M0 4h8" stroke="#8aa0b2" stroke-width="1.6"/></svg>Relieves Tension</li>
    </ul>

    <div class="tagline-band">Release. Relief. Repeat</div>
  </section>
</body>
</html>
```